Sales Tip from Ned Valcourt- Think Like a Buyer-

I am a sales trainer for B2B sales teams. I would like you to create an infographic that my learners can view, easily understand and immediately apply to their day to day work.
The graphic should:
1-Display the title on top- Sales Tip from Ned Valcourt- Think Like a Buyer
2- Please use the writing and layout from the attachment.
3- Create a tagline at the bottom that says- Top B2B Sales Teams, Sell The Way Thier Clients Buy.
Our company colors are red, silver with slight black trim.
I do not like cartoon like graphics. This must be poweful...
Updates

thank you very much for your consideration. looking forward to seeing your work Ned

Target Market(s)

CEO's of B2B Technology Companies

Font styles to use
Sans Serif

Requirements
Must have
• the apility to attach to a powerpoint slide. company colors...red, silver and a little black
Should not have
• cartoon animation, business,

```html
<!DOCTYPE html>
<html lang="en">
<head>
<meta charset="utf-8">
<title>Think Like a Buyer – Sales Tip from Ned Valcourt</title>
<link href="https://fonts.googleapis.com/css2?family=Arimo:wght@700&family=Source+Sans+3:wght@400;600;700&display=swap" rel="stylesheet">
<style>
  :root {
    --red: #e41f26;
    --red-light: #ef7070;
    --red-dark: #d12a25;
    --ink: #1a1a1a;
    --slate: #3d3d3f;
    --charcoal: #4a4a4c;
    --silver: #8e8f92;
    --green: #3bb44a;
    --paper: #ffffff;
    --rule: #1a1a1a;
  }
  * { margin: 0; padding: 0; box-sizing: border-box; }
  html, body { width: 1200px; height: 933px; overflow: hidden; background: var(--paper); }
  .canvas {
    position: relative; width: 1200px; height: 933px; overflow: hidden;
    font-family: "Source Sans 3", "Segoe UI", sans-serif; color: var(--ink);
  }
  .abs { position: absolute; }
  .graphics { position: absolute; left: 0; top: 0; }
  .kicker {
    left: 0; width: 1200px; top: 54px; text-align: center;
    font-size: 40px; font-weight: 400; letter-spacing: -0.2px;
  }
  .kicker strong { font-weight: 700; }
  .headline {
    left: 0; width: 1200px; top: 104px; text-align: center;
    font-family: "Arimo", "Helvetica", sans-serif; font-weight: 700;
    font-size: 92px; letter-spacing: -2px; color: var(--red); line-height: 1;
  }
  .col-head {
    top: 242px; height: 70px; display: flex; align-items: center; justify-content: center;
    color: var(--paper); font-weight: 700; font-size: 35px; letter-spacing: 2px;
  }
  .col-head--seller { left: 63px; width: 537px; }
  .col-head--buyer { left: 601px; width: 535px; padding-bottom: 8px; }
  .num {
    transform: translateY(-50%); font-weight: 700; font-size: 60px; line-height: 1;
  }
  .num--seller { left: 78px; color: var(--red); }
  .num--buyer { left: 630px; color: var(--slate); }
  .item {
    transform: translateY(-50%); font-size: 24px; line-height: 29px; color: var(--ink);
  }
  .item--seller { left: 163px; width: 440px; }
  .item--buyer { left: 705px; width: 440px; }
  .tagline {
    left: 0; width: 1200px; top: 766px; text-align: center;
    font-weight: 700; font-size: 35px; line-height: 36px; letter-spacing: -0.8px; color: var(--charcoal);
  }
</style>
</head>
<body>
<div class="canvas">
  <svg class="graphics" width="1200" height="933" viewBox="0 0 1200 933" aria-hidden="true">
    <defs>
      <linearGradient id="sellerBand" x1="0" x2="1" y1="0" y2="0">
        <stop offset="0" stop-color="var(--red-light)"/>
        <stop offset="1" stop-color="var(--red-dark)"/>
      </linearGradient>
      <linearGradient id="buyerBand" x1="0" x2="1" y1="0" y2="0">
        <stop offset="0" stop-color="#3e3e40"/>
        <stop offset="1" stop-color="var(--silver)"/>
      </linearGradient>
      <linearGradient id="footBand" x1="0" x2="1" y1="0" y2="0">
        <stop offset="0" stop-color="var(--red-light)"/>
        <stop offset="1" stop-color="var(--red-dark)"/>
      </linearGradient>
    </defs>
    <!-- buyer focus ring -->
    <circle cx="885" cy="479" r="266" fill="none" stroke="var(--green)" stroke-width="4"/>
    <!-- column heads -->
    <rect x="63" y="242" width="537" height="70" fill="url(#sellerBand)"/>
    <rect x="601" y="242" width="535" height="70" fill="url(#buyerBand)"/>
    <!-- seller rules -->
    <g stroke="var(--rule)" stroke-width="2">
      <line x1="137" x2="600" y1="389" y2="389"/>
      <line x1="137" x2="600" y1="469" y2="469"/>
      <line x1="137" x2="600" y1="548" y2="548"/>
      <line x1="137" x2="600" y1="629" y2="629"/>
      <line x1="680" x2="1136" y1="469" y2="469"/>
      <line x1="680" x2="1136" y1="548" y2="548"/>
      <line x1="680" x2="1136" y1="629" y2="629"/>
      <line x1="680" x2="1136" y1="709" y2="709"/>
    </g>
    <!-- footer band -->
    <polygon points="0,866 1200,849 1200,933 0,933" fill="url(#footBand)"/>
    <polygon points="0,866 440,914 0,933" fill="var(--red-light)" opacity="0.7"/>
  </svg>

  <div class="abs kicker">Sales Tip from <strong>Ned Valcourt</strong></div>
  <h1 class="abs headline">THINK LIKE A BUYER</h1>

  <div class="abs col-head col-head--seller">SELLER</div>
  <div class="abs col-head col-head--buyer">BUYER</div>

  <div class="abs num num--seller" style="top:360px">1</div>
  <div class="abs item item--seller" style="top:357px">Do they like us ?</div>
  <div class="abs num num--seller" style="top:435px">2</div>
  <div class="abs item item--seller" style="top:427px">Do they like our product or services better than our competition?</div>
  <div class="abs num num--seller" style="top:512px">3</div>
  <div class="abs item item--seller" style="top:507px">Will they accept our price ?</div>
  <div class="abs num num--seller" style="top:591px">4</div>
  <div class="abs item item--seller" style="top:587px">Can we close it quickly without being too pushy ?</div>

  <div class="abs num num--buyer" style="top:362px">1</div>
  <div class="abs item item--buyer" style="top:354px">How will this impact our business positively ?</div>
  <div class="abs num num--buyer" style="top:435px">2</div>
  <div class="abs item item--buyer" style="top:431px">What risks or disruptions could occur ? How do we mitigate them ?</div>
  <div class="abs num num--buyer" style="top:512px">3</div>
  <div class="abs item item--buyer" style="top:507px">Why do we need to do this now ?</div>
  <div class="abs num num--buyer" style="top:592px">4</div>
  <div class="abs item item--buyer" style="top:588px">Why them and not their competition ?</div>
  <div class="abs num num--buyer" style="top:671px">5</div>
  <div class="abs item item--buyer" style="top:665px">What are all of the costs involved ? Is the price fair market?</div>

  <p class="abs tagline">The Most Successful B2B Sales Teams<br>Sell The Way That Their Prospects Evaluate and Buy.</p>
</div>
</body>
</html>
```